Process Engineering/Construction Firm wants a OneSheet targeting craft brewers in Texas

We need a OneSheet (standard letter size) that we can share with craft brewers in our state, that explains what we can do for them. This will be shared primarily via email and online. We would like to see this be fun and modern flyer while still maintaining our professional vibe. More info and logos are uploaded - please review. Also, this project could lead to more branded documents from OneSheets to letterhead. We have our website and our logo(s) and really not much else that is consistent. There is certainly opportunity to work long-term.
Updates

Please note that the website listed on the flyer should read www.harrowfieldpartnersadvisory.com. It will NOT follow the same domain name as the email address. And also, please DO NOT send me anything through the sales@hfwadvisingllc.com email address at this time. I am trying to find a brewery-specific photo to use and will upload once found. I will be uploading shortly another logo of an affiliate organization we belong to - the Lone Kettle Maltsters' League that I would like to see included on the flyer with the words, "A proud member of the Lone Kettle Maltsters' League' OR just 'Proud Member.'

Target Market(s)

Craft brewery owners in Texas

Industry/Entity Type

Engineering

Font styles to use
Sans Serif

Requirements
Must have
• We need our point of contact to list the website as well as this email: sales@hfwadvisingllc.com
• Maroon CMYK is: 32, 100, 82, 30
• We want these Brewery Specific service points included:
• • Brewhouse automation
• • Glycol systems
• • Complete line design and install
• • Packaging solutions
• • Epoxy & urethane flooring
• • New construction
• • Network of industry professionals
Nice to have
• Trendy and modern look to correlate with current craft beer logos and design trends

```html
<!DOCTYPE html>
<html lang="en">
<head>
<meta charset="utf-8">
<title>Harrowfield Partners – Brewery Services OneSheet</title>
<link href="https://fonts.googleapis.com/css2?family=Montserrat:wght@500;600;700;800&display=swap" rel="stylesheet">
<style>
  :root {
    --maroon: #7a1622;
    --maroon-deep: #5e0f18;
    --amber: #f2a51c;
    --amber-light: #f7bd3a;
    --foam: #fbf6ea;
    --footer: #232323;
    --footer-top: #3a3a3a;
    --ink: #1c1c1c;
    --white: #ffffff;
    --orange: #f29a1f;
    --slate: #3b3b3d;
    --blue: #1f8fe6;
    --tangerine: #f0861c;
    --purple: #6b2aa3;
    --gold: #f2ab2a;
    --green: #56a92a;
  }
  * { margin: 0; padding: 0; box-sizing: border-box; }
  html, body { width: 927px; height: 1200px; overflow: hidden; background: var(--white); }
  .onesheet {
    position: relative;
    width: 927px;
    height: 1200px;
    overflow: hidden;
    font-family: "Montserrat", Arial, sans-serif;
    background: var(--maroon);
  }
  .hero-photo {
    position: absolute;
    left: 0; top: 0;
    width: 927px; height: 560px;
    background:
      radial-gradient(ellipse at 62% 25%, #e9e6e1 0%, rgba(233,230,225,0) 45%),
      radial-gradient(ellipse at 30% 60%, #8c8174 0%, rgba(140,129,116,0) 50%),
      linear-gradient(180deg, #cfd2d3 0%, #a9a49c 45%, #8a7f72 100%);
  }
  .brand {
    position: absolute;
    left: 80px; top: 72px;
    padding: 14px 22px 12px;
    background: rgba(255,255,255,0.88);
    border-radius: 4px;
  }
  .brand-name {
    display: block;
    font-size: 27px;
    font-weight: 800;
    color: var(--ink);
    letter-spacing: 0.2px;
  }
  .brand-tagline {
    display: block;
    margin-top: 4px;
    font-size: 10px;
    font-weight: 600;
    letter-spacing: 2.6px;
    color: var(--ink);
    text-align: center;
  }
  .waves {
    position: absolute;
    left: 0; top: 0;
    width: 927px; height: 1200px;
  }
  .services {
    position: absolute;
    left: 0; top: 0;
    width: 927px; height: 1200px;
  }
  .service-label {
    position: absolute;
    width: 200px;
    text-align: center;
    color: var(--white);
    font-size: 16.5px;
    font-weight: 600;
    line-height: 22px;
    text-transform: uppercase;
  }
  .contact-bar {
    position: absolute;
    left: 0; top: 1098px;
    width: 927px; height: 102px;
    background: linear-gradient(180deg, var(--footer-top) 0%, var(--footer) 40%, #1a1a1a 100%);
    display: flex;
    align-items: center;
    padding-left: 132px;
    gap: 42px;
    color: var(--white);
    font-size: 19.5px;
    font-weight: 500;
  }
</style>
</head>
<body>
<main class="onesheet">
  <div class="hero-photo" role="img" aria-label="Photo of three smiling young brewers holding glasses of beer beside stainless steel brewhouse tanks"></div>

  <div class="brand">
    <span class="brand-name">Harrowfield Partners</span>
    <span class="brand-tagline">ENGINEERING · CONSTRUCTION</span>
  </div>

  <svg class="waves" viewBox="0 0 927 1200" aria-hidden="true">
    <path fill="var(--foam)" d="M0 500 C 60 430, 120 560, 210 480 C 300 400, 350 520, 450 470 C 540 425, 600 520, 690 470 C 780 420, 840 500, 927 450 L 927 640 L 0 640 Z"/>
    <path fill="var(--amber)" d="M0 535 C 70 480, 130 590, 220 520 C 310 450, 360 560, 460 510 C 550 465, 610 555, 700 505 C 790 460, 850 530, 927 490 L 927 650 L 0 650 Z"/>
    <circle cx="62" cy="625" r="6" fill="var(--amber-light)"/>
    <circle cx="140" cy="588" r="4" fill="var(--foam)" opacity="0.7"/>
    <circle cx="330" cy="610" r="5" fill="var(--amber-light)"/>
    <circle cx="610" cy="580" r="4" fill="var(--foam)" opacity="0.7"/>
    <circle cx="820" cy="600" r="7" fill="var(--amber-light)"/>
    <path fill="var(--maroon)" d="M0 598 L 927 640 L 927 1080 L 0 1080 Z"/>
    <circle cx="90" cy="700" r="5" fill="var(--maroon-deep)"/>
    <circle cx="860" cy="760" r="7" fill="var(--maroon-deep)"/>
    <circle cx="60" cy="980" r="6" fill="var(--maroon-deep)"/>
    <circle cx="880" cy="990" r="5" fill="var(--maroon-deep)"/>
    <path fill="var(--amber)" d="M0 1058 L 927 1052 L 927 1070 L 0 1072 Z"/>
    <rect x="0" y="1070" width="927" height="30" fill="var(--maroon-deep)"/>
  </svg>

  <svg class="services" viewBox="0 0 927 1200" aria-hidden="true">
    <defs>
      <path id="puzzle" d="M-48 -48 H-14 A14 14 0 1 1 14 -48 H48 V-14 A14 14 0 1 1 48 14 V48 H14 A14 14 0 1 0 -14 48 H-48 Z"/>
    </defs>

    <g transform="translate(160 742)">
      <use href="#puzzle" fill="var(--orange)"/>
      <g fill="none" stroke="var(--white)" stroke-width="3">
        <circle cx="-12" cy="-10" r="14"/><circle cx="-12" cy="-10" r="5"/>
        <circle cx="16" cy="14" r="11"/><circle cx="16" cy="14" r="4"/>
      </g>
    </g>
    <g transform="translate(338 742)">
      <use href="#puzzle" fill="var(--slate)"/>
      <g fill="none" stroke="var(--white)" stroke-width="3" stroke-linecap="round">
        <path d="M-30 -12 H10 V4"/><path d="M-30 -2 H0 V4"/><path d="M-10 -24 V-12"/><path d="M-18 -24 H-2"/>
        <path d="M5 16 C 5 24, 13 28, 13 20 C 13 16, 9 12, 9 10"/>
      </g>
    </g>
    <g transform="translate(566 742)">
      <use href="#puzzle" fill="var(--blue)"/>
      <g fill="none" stroke="var(--white)" stroke-width="3" stroke-linejoin="round">
        <rect x="-30" y="-26" width="56" height="46"/><path d="M-30 -10 H26"/><path d="M-8 8 L18 -22 L24 -16 L-2 14 Z"/>
      </g>
    </g>
    <g transform="translate(776 742)">
      <use href="#puzzle" fill="var(--tangerine)"/>
      <g fill="none" stroke="var(--white)" stroke-width="3" stroke-linejoin="round">
        <path d="M-7 -34 H7 V-20 L14 -8 V30 H-14 V-8 L-7 -20 Z"/><path d="M-14 2 H14"/>
      </g>
    </g>

    <g transform="translate(255 932)">
      <use href="#puzzle" fill="var(--purple)"/>
      <g fill="none" stroke="var(--white)" stroke-width="3">
        <rect x="-30" y="-28" width="44" height="56"/><path d="M-30 -8 H14 M-30 10 H14 M-16 -28 V28 M0 -28 V28"/>
        <path d="M24 -10 C 24 -2, 32 -2, 32 -10 L28 -20 Z"/>
      </g>
    </g>
    <g transform="translate(458 932)">
      <use href="#puzzle" fill="var(--gold)"/>
      <g fill="none" stroke="var(--white)" stroke-width="3" stroke-linecap="round">
        <path d="M-20 30 V-30 M-32 -24 H30 M18 -24 V-6"/><rect x="-8" y="-2" width="30" height="32"/>
        <path d="M-2 8 H16 M-2 18 H16"/>
      </g>
    </g>
    <g transform="translate(668 932)">
      <use href="#puzzle" fill="var(--green)"/>
      <g fill="none" stroke="var(--white)" stroke-width="3">
        <path d="M-20 -18 L0 0 L20 -18 M0 0 L-22 20 M0 0 L22 20"/>
        <circle cx="0" cy="0" r="8"/><circle cx="-22" cy="-20" r="7"/><circle cx="22" cy="-20" r="7"/>
        <circle cx="-24" cy="22" r="7"/><circle cx="24" cy="22" r="7"/>
      </g>
    </g>
  </svg>

  <p class="service-label" style="left:42px; top:806px;">Brewhouse<br>Automation</p>
  <p class="service-label" style="left:256px; top:806px;">Glycol<br>Systems</p>
  <p class="service-label" style="left:466px; top:806px;">Complete Line<br>Design and Install</p>
  <p class="service-label" style="left:685px; top:806px;">Packaging<br>Solutions</p>
  <p class="service-label" style="left:140px; top:998px;">Epoxy &amp; Urethane<br>Flooring</p>
  <p class="service-label" style="left:360px; top:998px;">New Construction</p>
  <p class="service-label" style="left:568px; top:998px;">Network of Indus-<br>try Professionals</p>

  <footer class="contact-bar">
    <span class="contact-email">sales@hfwadvisingllc.com</span>
    <span class="contact-web">www.harrowfieldpartnersadvisory.com</span>
  </footer>
</main>
</body>
</html>
```